Carpentry and Building Business Card

I'm looking for a business card that is minimalistic and that incorporates the theme of my Velmor logo.
On one side I'd like the VELMOR logo with my details on the other side.
Double sided with curved edges

Target Market(s)

Construction / renovation
Adults

Industry/Entity Type

Tradesman

Contact Information for Business Card

Logo on one side, details on the other

Colors

Designer to choose only greyscale colors for use in the design.

Requirements
Must have
• Nilo Petrakis
VELMOR CONSTRUCT
Carpentry & Building Services
0481236574
Velmorconstruct@brixmail.com
Lic No. 718263D
Nice to have
• Fb and insta icons. @velmorconstruct
Should not have
• No hammer or tool icons please.

No address line.

```html
<!DOCTYPE html>
<html lang="en">
<head>
<meta charset="utf-8">
<title>Velmor Construct – Business Card</title>
<link rel="stylesheet" href="https://fonts.googleapis.com/css2?family=Montserrat:wght@400;500;600&family=Arimo:wght@400;700&display=swap">
<style>
  :root {
    --bg: #161616;
    --ink: #231f20;
    --paper: #ffffff;
    --accent: #ee9a3f;
    --muted: #d9d9d9;
  }
  * { box-sizing: border-box; margin: 0; padding: 0; }
  html, body {
    width: 1200px; height: 1015px; overflow: hidden;
    background: var(--bg);
  }
  .canvas {
    position: relative; width: 1200px; height: 1015px;
    display: flex; flex-direction: column; align-items: center; justify-content: center; gap: 60px;
  }
  .card {
    position: relative; width: 700px; height: 400px; overflow: hidden;
    box-shadow: 0 18px 40px rgba(0,0,0,.6);
  }
  .card__bg { position: absolute; inset: 0; width: 100%; height: 100%; }
  .wordmark {
    position: absolute; display: flex; align-items: center; gap: 20px;
    font-family: "Montserrat", sans-serif; font-weight: 500;
    color: var(--ink); letter-spacing: 0.28em; font-size: 40px; line-height: 1;
    white-space: nowrap;
  }
  .wordmark__square {
    width: 54px; height: 54px; border: 3px solid var(--accent); flex: none;
  }
  .card--front .wordmark { left: 318px; top: 238px; }
  .social {
    position: absolute; left: 46px; top: 58px; display: flex; align-items: center; gap: 12px;
    font-family: "Arimo", sans-serif; font-size: 17px; color: var(--muted);
  }
  .social__mark { width: 20px; height: 20px; background: var(--accent); border-radius: 4px; }
  .card--back .wordmark { left: 44px; top: 84px; }
  .details {
    position: absolute; right: 40px; top: 218px; text-align: right;
    font-family: "Arimo", sans-serif; color: var(--muted);
  }
  .details__name {
    font-family: "Montserrat", sans-serif; font-weight: 600; font-size: 24px;
    color: var(--accent); letter-spacing: 0.01em;
  }
  .details__role { font-size: 16px; margin-top: 2px; }
  .details__contact { margin-top: 18px; font-size: 16px; line-height: 1.5; }
  .details__contact li { list-style: none; display: flex; justify-content: flex-end; align-items: center; gap: 8px; }
  .details__icon { width: 14px; height: 14px; }
  .licence {
    position: absolute; left: 40px; bottom: 22px;
    font-family: "Arimo", sans-serif; font-size: 18px; color: var(--muted);
  }
  .licence__label { color: var(--accent); }
</style>
</head>
<body>
<main class="canvas">

  <section class="card card--front" aria-label="Card front">
    <svg class="card__bg" viewBox="0 0 700 400" preserveAspectRatio="none" aria-hidden="true">
      <rect width="700" height="400" fill="var(--ink)"/>
      <path d="M0,322 C140,316 200,290 250,220 C320,120 420,44 560,26 C620,20 670,20 700,20" fill="none" stroke="var(--paper)" stroke-width="4"/>
      <path d="M0,336 C150,330 210,304 262,234 C332,134 430,58 566,40 C624,34 672,34 700,34 L700,400 L0,400 Z" fill="var(--ink)"/>
      <path d="M0,346 C156,340 218,314 272,244 C342,146 438,70 572,52 C628,46 674,46 700,46 L700,400 L0,400 Z" fill="var(--paper)"/>
      <path d="M360,150 C420,100 480,74 578,64 C630,58 674,58 700,58" fill="none" stroke="var(--accent)" stroke-width="5"/>
    </svg>
    <div class="social">
      <span class="social__mark"></span>
      <span>@velmorconstruct</span>
    </div>
    <div class="wordmark">
      <span class="wordmark__square"></span>
      <span>VELMOR.</span>
    </div>
  </section>

  <section class="card card--back" aria-label="Card back">
    <svg class="card__bg" viewBox="0 0 700 400" preserveAspectRatio="none" aria-hidden="true">
      <rect width="700" height="400" fill="var(--paper)"/>
      <path d="M0,300 C200,300 330,270 430,180 C510,112 590,96 700,92" fill="none" stroke="var(--accent)" stroke-width="6"/>
      <path d="M0,320 C210,320 342,290 444,200 C524,132 600,114 700,110" fill="none" stroke="var(--ink)" stroke-width="8"/>
      <path d="M0,336 C216,336 352,306 456,216 C536,148 608,130 700,126 L700,400 L0,400 Z" fill="var(--ink)"/>
    </svg>
    <div class="wordmark">
      <span class="wordmark__square"></span>
      <span>VELMOR.</span>
    </div>
    <div class="details">
      <p class="details__name">NILO PETRAKIS</p>
      <p class="details__role">Carpentry &amp; Building Services</p>
      <ul class="details__contact">
        <li>0481236574
          <svg class="details__icon" viewBox="0 0 16 16" aria-hidden="true"><path d="M3 1h3l1.5 4-2 1.3a9 9 0 0 0 4.2 4.2L11 8.5l4 1.5v3a2 2 0 0 1-2 2A12 12 0 0 1 1 3a2 2 0 0 1 2-2z" fill="var(--accent)"/></svg>
        </li>
        <li>Velmorconstruct@brixmail.com
          <svg class="details__icon" viewBox="0 0 16 16" aria-hidden="true"><rect x="1" y="3" width="14" height="10" fill="var(--accent)"/><path d="M1 3l7 6 7-6" fill="none" stroke="var(--ink)" stroke-width="1.2"/></svg>
        </li>
      </ul>
    </div>
    <p class="licence"><span class="licence__label">LIC NO.</span> 718263D</p>
  </section>

</main>
</body>
</html>
```